Business Cards for Communications Technology Company

We are an innovative software company based in Tropical North Queensland, Australia. We have several brands with a focus on communications software for businesses. We are looking for a business card that is very innovate and creative whilst still remaining professional on a corporate level.

Our internal culture is very progressive and expresses a blend between the clarity of our natural surroundings and the highly technological industry we work in. Our current branding blends a modern minimalist typeface with the desire to push the boundaries in the way we communicate.

This is a corporate level business card for the communications software industry and may possibly also encompass our brands MarNetwork, PelFax, TukMailer and our B2B marketing service—with our companies name being Viresca Partners. Showing other brands on the business card is optional not compulsory.

Technical notes:

-We will attach all logo's and some examples of our corporate branding
- Would be willing to print with various papers, embossed, metallic ink, curved edges etc. in a standard business card size

Sample content:

Rowan Pellick
Senior Account Manager
Phone: 1300 842 916 / +617 4583 2764
Email: r.pellick@viresca.com.au
Web: www.viresca.com.au

Sincerely,
Viresca Partners.

```html
<!DOCTYPE html>
<html lang="en">
<head>
<meta charset="utf-8">
<title>Viresca Partners – Business Card</title>
<link rel="stylesheet" href="https://fonts.googleapis.com/css2?family=Montserrat:wght@600;700&display=swap">
<style>
  :root {
    --paper: #ffffff;
    --panel: #3b3b3b;
    --steel-dark: #5e6166;
    --steel-mid: #9a9da2;
    --steel-light: #eeeeee;
    --brand-orange: #ec6a23;
    --brand-blue: #0f6fe8;
    --brand-green: #72b83a;
    --wordmark: #6e7176;
  }
  html, body {
    margin: 0;
    padding: 0;
    width: 1200px;
    height: 1000px;
    overflow: hidden;
    background: var(--paper);
  }
  .card {
    position: relative;
    width: 1200px;
    height: 1000px;
    font-family: "Montserrat", Arial, sans-serif;
  }
  .card-art {
    position: absolute;
    inset: 0;
  }
  .company-lockup {
    position: absolute;
    left: 160px;
    top: 310px;
    display: flex;
    align-items: center;
    gap: 34px;
  }
  .company-dot {
    width: 150px;
    height: 150px;
    border-radius: 50%;
    background: var(--steel-mid);
  }
  .company-name {
    margin: 0;
    font-size: 84px;
    font-weight: 700;
    letter-spacing: 1px;
    color: var(--wordmark);
    line-height: 1;
  }
  .brand {
    position: absolute;
    top: 598px;
    width: 300px;
    display: flex;
    flex-direction: column;
    align-items: center;
    gap: 22px;
  }
  .brand-disc {
    width: 92px;
    height: 92px;
    border-radius: 50%;
    background: var(--paper);
    box-shadow: 0 0 0 5px var(--steel-mid), 0 0 0 7px var(--steel-light);
  }
  .brand-name {
    margin: 0;
    font-size: 46px;
    font-weight: 700;
    line-height: 1;
  }
  .brand--network { left: 108px; }
  .brand--network .brand-name { color: var(--brand-orange); }
  .brand--mailer { left: 473px; }
  .brand--mailer .brand-name { color: var(--brand-blue); }
  .brand--fax { left: 828px; }
  .brand--fax .brand-name { color: var(--brand-green); }
</style>
</head>
<body>
<main class="card">
  <svg class="card-art" width="1200" height="1000" viewBox="0 0 1200 1000" aria-hidden="true">
    <defs>
      <linearGradient id="steel-band" x1="0" y1="0" x2="1" y2="0">
        <stop offset="0" stop-color="#8a8d92"/>
        <stop offset="0.15" stop-color="#f2f2f2"/>
        <stop offset="0.3" stop-color="#6a6d72"/>
        <stop offset="0.45" stop-color="#d9d9d9"/>
        <stop offset="0.55" stop-color="#7c7f84"/>
        <stop offset="0.7" stop-color="#f5f5f5"/>
        <stop offset="0.85" stop-color="#75787d"/>
        <stop offset="1" stop-color="#e8e8e8"/>
      </linearGradient>
    </defs>
    <path class="dark-panel" fill="var(--panel)"
      d="M68,600 C150,520 300,495 450,500 C650,508 800,545 950,520 C1030,508 1080,480 1120,458 L1120,695 Q1120,785 1030,785 L68,785 Z"/>
    <path class="steel-wave" fill="none" stroke="url(#steel-band)" stroke-width="22"
      d="M68,596 C150,516 300,491 450,496 C650,504 800,541 950,516 C1030,504 1080,476 1120,454"/>
  </svg>

  <div class="company-lockup">
    <span class="company-dot"></span>
    <h1 class="company-name">Viresca Partners</h1>
  </div>

  <div class="brand brand--network">
    <span class="brand-disc"></span>
    <p class="brand-name">MarNetwork</p>
  </div>
  <div class="brand brand--mailer">
    <span class="brand-disc"></span>
    <p class="brand-name">TukMailer</p>
  </div>
  <div class="brand brand--fax">
    <span class="brand-disc"></span>
    <p class="brand-name">PelFax</p>
  </div>
</main>
</body>
</html>
```